Musical download and streaming website

hello designers, I want to start up a musical website where users can download and rate music of different genres such as RnB, Hip hop, rock, afro-pop. This website should be attractive and contemporary. There will be a search column for different songs. Music files will be mp3, mwa, and others. I like blue, gold, pink and indigo colors. My website should resemble http://qorvitune.net. There should be good imaginary of music stars on my website.

```html
<!DOCTYPE html>
<html lang="en">
<head>
<meta charset="utf-8">
<title>Corva Music</title>
<link href="https://fonts.googleapis.com/css2?family=Raleway:wght@400;500;600;700&display=swap" rel="stylesheet">
<style>
:root{
  --blue:#1565c0;
  --blue-deep:#0d4fa6;
  --link:#1f66c9;
  --pink:#e3168a;
  --pink-dark:#c90b74;
  --gold:#a9733c;
  --indigo:#4a0e8f;
  --plum:#4b1070;
  --text:#444;
  --panel:#f1f1f1;
  --line:#dcdcdc;
  --white:#fff;
}
*{box-sizing:border-box;margin:0;padding:0}
html,body{width:682px;height:1200px;overflow:hidden}
body{font-family:'Raleway',sans-serif;color:var(--text);background:var(--white);position:relative}
.site-header{height:42px;display:flex;align-items:center;padding:0 42px;position:relative}
.logo{font-size:27px;font-weight:500;color:var(--blue);letter-spacing:.3px;width:168px;white-space:nowrap}
.main-nav{display:flex;gap:23px;margin-left:35px;font-size:7.5px;font-weight:600;color:#222;letter-spacing:.3px}
.main-nav .active{color:var(--blue)}
.search-toggle{position:absolute;right:42px;top:16px}
.hero{position:relative;height:332px;overflow:hidden}
.hero-photo{position:absolute;inset:0;background:
  radial-gradient(ellipse 40% 45% at 30% 10%,#b9a21d 0%,rgba(140,110,20,.5) 45%,transparent 75%),
  radial-gradient(ellipse 30% 40% at 65% 35%,#7a3d25 0%,transparent 70%),
  radial-gradient(ellipse 35% 30% at 80% 75%,#3a3a3a 0%,transparent 70%),
  linear-gradient(160deg,#3b2d0a 0%,#1f1409 45%,#120c08 100%)}
.hero-content{position:absolute;left:42px;top:97px}
.hero-title{font-size:29px;font-weight:700;color:var(--white);line-height:36px}
.search-box{margin-top:6px;width:306px;height:32px;background:var(--white);display:flex;align-items:center;padding:0 4px 0 10px}
.search-box input{flex:1;border:0;font:600 8px 'Raleway',sans-serif;color:#555;margin-left:7px;outline:none;background:transparent}
.search-btn{width:72px;height:22px;background:var(--indigo);color:var(--white);border:0;font:700 8px 'Raleway',sans-serif;letter-spacing:.4px}
.filters{display:flex;gap:10px;margin-top:13px;font-size:6.5px;font-weight:600;color:var(--white)}
.filters span{display:flex;align-items:center;gap:3px}
.box{width:6px;height:6px;border:1px solid var(--white)}
.dots{position:absolute;left:42px;top:343px;display:flex;gap:4px}
.dots i{width:5px;height:5px;border-radius:50%;background:var(--white)}
.dots i:first-child{background:var(--pink)}
.quick-links{display:flex;justify-content:space-between;padding:26px 42px}
.quick-btn{width:188px;height:31px;background:linear-gradient(var(--pink),var(--pink-dark));color:var(--white);display:flex;align-items:center;justify-content:center;gap:8px;font-size:9.5px;font-weight:700}
.updates{background:var(--blue);height:208px;padding:19px 42px 0}
.updates-head{display:flex;justify-content:space-between;align-items:center;color:var(--white)}
.updates-head h2{font-size:11px;font-weight:500}
.arrows{display:flex;gap:2px}
.cards{display:flex;justify-content:space-between;margin-top:16px}
.card{width:138px;background:var(--white)}
.card-img{height:77px}
.img-rnb{background:linear-gradient(#2c4f7e,#9ab0c8 60%,#d9e2ea)}
.img-hiphop{background:linear-gradient(135deg,#6b6c5c,#353b33 60%,#8c8b77)}
.img-rock{background:radial-gradient(circle at 35% 55%,#f2c23a,#d6581c 40%,#3f7fb7 80%)}
.img-afro{background:linear-gradient(135deg,#e8b778,#c57a45 55%,#f0c88f)}
.card-body{padding:8px 9px 0;height:42px}
.card-title{display:flex;justify-content:space-between;font-size:8px;font-weight:700;color:var(--plum)}
.stars{color:var(--gold);font-size:7px;letter-spacing:.5px}
.card-text{font-size:8px;color:#444;margin-top:7px}
.card-foot{border-top:1px solid #e4e4e4;height:20px;display:flex;align-items:center;justify-content:space-between;padding:0 9px;font-size:7px;font-weight:600;color:var(--pink)}
.card-foot span{display:flex;align-items:center;gap:4px}
.lists{display:flex;justify-content:space-between;padding:26px 42px 0}
.list-panel{width:188px;height:225px;background:var(--panel)}
.list-panel h3{height:28px;background:var(--gold);color:var(--white);font-size:11px;font-weight:500;padding:8px 10px}
.list-panel ul{list-style:none;margin:7px 13px 0}
.list-panel li{display:flex;align-items:center;height:23.6px;border-bottom:1px solid var(--line);font-size:8px;color:#555}
.list-panel li:last-child{border-bottom:0}
.list-panel li svg{margin-right:6px}
.list-panel li b{margin-left:auto;color:var(--link);font-weight:600;font-size:7.5px}
.more-btn{margin:6px 0 0 12px;width:69px;height:21px;background:var(--pink);color:var(--white);font-size:7.5px;font-weight:700;display:flex;align-items:center;justify-content:center}
.about{position:absolute;top:942px;left:0;width:682px;height:152px;background:var(--panel)}
.about-text{position:absolute;left:42px;top:24px;width:393px}
.about-text h2{font-size:11px;font-weight:500;color:var(--blue)}
.about-text p{font-size:8.8px;line-height:14.6px;color:#444;margin-top:9px}
.about-text a{display:block;margin-top:6px;font-size:8.5px;color:var(--pink-dark);text-decoration:underline}
.signup{position:absolute;left:451px;top:19px;width:189px;height:115px;background:var(--gold);padding:12px 12px}
.signup h3{font-size:11px;font-weight:500;color:var(--white)}
.signup p{font-size:8.8px;font-style:italic;color:#f2dfc8;margin-top:4px;line-height:13px}
.signup input{display:block;width:100%;height:20px;border:0;margin-top:7px;padding:0 6px;font:7px 'Raleway',sans-serif;color:#777;outline:none}
.signup button{display:block;margin:7px 0 0 auto;width:69px;height:20px;background:var(--pink);border:0;color:var(--white);font:700 8px 'Raleway',sans-serif}
.site-footer{position:absolute;top:1094px;left:0;width:682px;height:106px;background:linear-gradient(var(--blue-deep),var(--blue));color:#dfe9f8;text-align:center;font-size:7px;padding-top:25px;line-height:13px}
.copyright{margin-top:7px;color:var(--white)}
.social{display:flex;justify-content:center;gap:13px;margin-top:8px}
.social i{width:9px;height:9px;border-radius:50%;border:1.5px solid #dfe9f8}
</style>
</head>
<body>
<header class="site-header">
  <div class="logo">Corva Music</div>
  <nav class="main-nav"><span class="active">HOME</span><span>RNB</span><span>HIP HOP</span><span>ROCK</span><span>AFRO-POP</span><span>DOWNLOADS</span></nav>
  <svg class="search-toggle" width="9" height="9" viewBox="0 0 10 10"><circle cx="4" cy="4" r="3" fill="none" stroke="#4a0e8f" stroke-width="1.6"/><path d="M6.3 6.3 9 9" stroke="#4a0e8f" stroke-width="1.8"/></svg>
</header>

<section class="hero">
  <div class="hero-photo" role="img" aria-label="Photo of a smiling female singer with headphones beside a laptop, warm golden light"></div>
  <div class="hero-content">
    <h1 class="hero-title">Search Music</h1>
    <form class="search-box">
      <svg width="8" height="8" viewBox="0 0 10 10"><circle cx="4" cy="4" r="3" fill="none" stroke="#555" stroke-width="1.6"/><path d="M6.3 6.3 9 9" stroke="#555" stroke-width="1.8"/></svg>
      <input type="text" placeholder="Search keywords here">
      <button class="search-btn" type="button">SEARCH</button>
    </form>
    <div class="filters">
      <span><svg width="7" height="7" viewBox="0 0 8 8"><rect x=".5" y=".5" width="7" height="7" fill="none" stroke="#fff"/><path d="M2 4l1.5 1.5L6.5 2" fill="none" stroke="#fff"/></svg>All</span>
      <span><i class="box"></i>Artist</span>
      <span><i class="box"></i>Category</span>
    </div>
  </div>
  <div class="dots"><i></i><i></i><i></i><i></i></div>
</section>

<section class="quick-links">
  <div class="quick-btn"><svg width="11" height="9" viewBox="0 0 12 9" fill="#fff"><circle cx="6" cy="2.2" r="2"/><circle cx="2.3" cy="3" r="1.5"/><circle cx="9.7" cy="3" r="1.5"/><path d="M2.5 9c0-3 7-3 7 0zM0 8c0-2 3-2.5 3-1.5V8zM12 8c0-2-3-2.5-3-1.5V8z"/></svg>Download by Artists</div>
  <div class="quick-btn"><svg width="9" height="9" viewBox="0 0 10 10" fill="#fff"><path d="M3.5 1.5 9 0v7.2a1.6 1.3 0 1 1-1-1.2V2L4.5 3v5.2a1.6 1.3 0 1 1-1-1.2z"/></svg>Download by Top Songs</div>
  <div class="quick-btn"><svg width="9" height="9" viewBox="0 0 9 9" fill="#fff"><rect width="2.5" height="2.5"/><rect x="3.25" width="2.5" height="2.5"/><rect x="6.5" width="2.5" height="2.5"/><rect y="3.25" width="2.5" height="2.5"/><rect x="3.25" y="3.25" width="2.5" height="2.5"/><rect x="6.5" y="3.25" width="2.5" height="2.5"/><rect y="6.5" width="2.5" height="2.5"/><rect x="3.25" y="6.5" width="2.5" height="2.5"/><rect x="6.5" y="6.5" width="2.5" height="2.5"/></svg>Download by Categories</div>
</section>

<section class="updates">
  <div class="updates-head">
    <h2>LATEST MUSIC UPDATES</h2>
    <div class="arrows">
      <svg width="10" height="10" viewBox="0 0 10 10"><circle cx="5" cy="5" r="5" fill="#fff"/><path d="M6 2.5 3.5 5 6 7.5" fill="none" stroke="#1565c0" stroke-width="1.6"/></svg>
      <svg width="10" height="10" viewBox="0 0 10 10"><circle cx="5" cy="5" r="5" fill="#fff"/><path d="M4 2.5 6.5 5 4 7.5" fill="none" stroke="#1565c0" stroke-width="1.6"/></svg>
    </div>
  </div>
  <div class="cards">
    <article class="card"><div class="card-img img-rnb" role="img" aria-label="Chrome RnB lettering artwork"></div>
      <div class="card-body"><div class="card-title">RnB<span class="stars">★★★★★</span></div><p class="card-text">Etiam pretium porttitor....</p></div>
      <div class="card-foot"><span><svg width="8" height="6" viewBox="0 0 10 7"><path d="M2.5 7a2.3 2.3 0 0 1-.3-4.6A3 3 0 0 1 8 2.5 2.3 2.3 0 0 1 8 7z" fill="#555"/><path d="M5 2.5v3M3.7 4.3 5 5.6l1.3-1.3" stroke="#fff" fill="none"/></svg>Download</span><svg width="7" height="7" viewBox="0 0 8 8" fill="#333"><circle cx="6.5" cy="1.5" r="1.4"/><circle cx="1.5" cy="4" r="1.4"/><circle cx="6.5" cy="6.5" r="1.4"/><path d="M6.5 1.5 1.5 4l5 2.5" stroke="#333" fill="none"/></svg></div></article>
    <article class="card"><div class="card-img img-hiphop" role="img" aria-label="Photo of hip hop dancers in front of a graffiti wall"></div>
      <div class="card-body"><div class="card-title">Hip Hop<span class="stars">★★★★★</span></div><p class="card-text">Etiam pretium porttitor....</p></div>
      <div class="card-foot"><span><svg width="8" height="6" viewBox="0 0 10 7"><path d="M2.5 7a2.3 2.3 0 0 1-.3-4.6A3 3 0 0 1 8 2.5 2.3 2.3 0 0 1 8 7z" fill="#555"/><path d="M5 2.5v3M3.7 4.3 5 5.6l1.3-1.3" stroke="#fff" fill="none"/></svg>Download</span><svg width="7" height="7" viewBox="0 0 8 8" fill="#333"><circle cx="6.5" cy="1.5" r="1.4"/><circle cx="1.5" cy="4" r="1.4"/><circle cx="6.5" cy="6.5" r="1.4"/><path d="M6.5 1.5 1.5 4l5 2.5" stroke="#333" fill="none"/></svg></div></article>
    <article class="card"><div class="card-img img-rock" role="img" aria-label="Photo of a rock guitarist with fire and water splash"></div>
      <div class="card-body"><div class="card-title">Rock<span class="stars">★★★★★</span></div><p class="card-text">Etiam pretium porttitor....</p></div>
      <div class="card-foot"><span><svg width="8" height="6" viewBox="0 0 10 7"><path d="M2.5 7a2.3 2.3 0 0 1-.3-4.6A3 3 0 0 1 8 2.5 2.3 2.3 0 0 1 8 7z" fill="#555"/><path d="M5 2.5v3M3.7 4.3 5 5.6l1.3-1.3" stroke="#fff" fill="none"/></svg>Download</span><svg width="7" height="7" viewBox="0 0 8 8" fill="#333"><circle cx="6.5" cy="1.5" r="1.4"/><circle cx="1.5" cy="4" r="1.4"/><circle cx="6.5" cy="6.5" r="1.4"/><path d="M6.5 1.5 1.5 4l5 2.5" stroke="#333" fill="none"/></svg></div></article>
    <article class="card"><div class="card-img img-afro" role="img" aria-label="Illustration of street musicians in a city"></div>
      <div class="card-body"><div class="card-title">Afro-Pop<span class="stars">★★★★★</span></div><p class="card-text">Etiam pretium porttitor....</p></div>
      <div class="card-foot"><span><svg width="8" height="6" viewBox="0 0 10 7"><path d="M2.5 7a2.3 2.3 0 0 1-.3-4.6A3 3 0 0 1 8 2.5 2.3 2.3 0 0 1 8 7z" fill="#555"/><path d="M5 2.5v3M3.7 4.3 5 5.6l1.3-1.3" stroke="#fff" fill="none"/></svg>Download</span><svg width="7" height="7" viewBox="0 0 8 8" fill="#333"><circle cx="6.5" cy="1.5" r="1.4"/><circle cx="1.5" cy="4" r="1.4"/><circle cx="6.5" cy="6.5" r="1.4"/><path d="M6.5 1.5 1.5 4l5 2.5" stroke="#333" fill="none"/></svg></div></article>
  </div>
</section>

<section class="lists">
  <div class="list-panel"><h3>LAST ADDED</h3>
    <ul>
      <li><svg width="8" height="6" viewBox="0 0 10 7"><path d="M2.5 7a2.3 2.3 0 0 1-.3-4.6A3 3 0 0 1 8 2.5 2.3 2.3 0 0 1 8 7z" fill="#555"/></svg>Duis aliquam nibh<b>4:25</b></li>
      <li><svg width="8" height="6" viewBox="0 0 10 7"><path d="M2.5 7a2.3 2.3 0 0 1-.3-4.6A3 3 0 0 1 8 2.5 2.3 2.3 0 0 1 8 7z" fill="#555"/></svg>Dui iaculis viverra id a velit<b>4:25</b></li>
      <li><svg width="8" height="6" viewBox="0 0 10 7"><path d="M2.5 7a2.3 2.3 0 0 1-.3-4.6A3 3 0 0 1 8 2.5 2.3 2.3 0 0 1 8 7z" fill="#555"/></svg>Vivamus egestas risus in<b>4:25</b></li>
      <li><svg width="8" height="6" viewBox="0 0 10 7"><path d="M2.5 7a2.3 2.3 0 0 1-.3-4.6A3 3 0 0 1 8 2.5 2.3 2.3 0 0 1 8 7z" fill="#555"/></svg>Magna varius commodo<b>4:25</b></li>
      <li><svg width="8" height="6" viewBox="0 0 10 7"><path d="M2.5 7a2.3 2.3 0 0 1-.3-4.6A3 3 0 0 1 8 2.5 2.3 2.3 0 0 1 8 7z" fill="#555"/></svg>Sed semper viverra<b>4:25</b></li>
      <li><svg width="8" height="6" viewBox="0 0 10 7"><path d="M2.5 7a2.3 2.3 0 0 1-.3-4.6A3 3 0 0 1 8 2.5 2.3 2.3 0 0 1 8 7z" fill="#555"/></svg>Egestas lobortis turpis<b>4:25</b></li>
    </ul>
    <div class="more-btn">SEE MORE</div>
  </div>
  <div class="list-panel"><h3>TOP 20 SONGS</h3>
    <ul>
      <li><svg width="8" height="6" viewBox="0 0 10 7"><path d="M2.5 7a2.3 2.3 0 0 1-.3-4.6A3 3 0 0 1 8 2.5 2.3 2.3 0 0 1 8 7z" fill="#555"/></svg>Duis aliquam nibh<b>4:25</b></li>
      <li><svg width="8" height="6" viewBox="0 0 10 7"><path d="M2.5 7a2.3 2.3 0 0 1-.3-4.6A3 3 0 0 1 8 2.5 2.3 2.3 0 0 1 8 7z" fill="#555"/></svg>Dui iaculis viverra id a velit<b>4:25</b></li>
      <li><svg width="8" height="6" viewBox="0 0 10 7"><path d="M2.5 7a2.3 2.3 0 0 1-.3-4.6A3 3 0 0 1 8 2.5 2.3 2.3 0 0 1 8 7z" fill="#555"/></svg>Vivamus egestas risus in<b>4:25</b></li>
      <li><svg width="8" height="6" viewBox="0 0 10 7"><path d="M2.5 7a2.3 2.3 0 0 1-.3-4.6A3 3 0 0 1 8 2.5 2.3 2.3 0 0 1 8 7z" fill="#555"/></svg>Magna varius commodo<b>4:25</b></li>
      <li><svg width="8" height="6" viewBox="0 0 10 7"><path d="M2.5 7a2.3 2.3 0 0 1-.3-4.6A3 3 0 0 1 8 2.5 2.3 2.3 0 0 1 8 7z" fill="#555"/></svg>Sed semper viverra<b>4:25</b></li>
      <li><svg width="8" height="6" viewBox="0 0 10 7"><path d="M2.5 7a2.3 2.3 0 0 1-.3-4.6A3 3 0 0 1 8 2.5 2.3 2.3 0 0 1 8 7z" fill="#555"/></svg>Egestas lobortis turpis<b>4:25</b></li>
    </ul>
    <div class="more-btn">SEE MORE</div>
  </div>
  <div class="list-panel"><h3>COMING SOON</h3>
    <ul>
      <li><svg width="7" height="7" viewBox="0 0 8 8"><circle cx="4" cy="4" r="4" fill="#555"/><path d="M4 3.3v3" stroke="#fff" stroke-width="1.2"/><circle cx="4" cy="2" r=".7" fill="#fff"/></svg>Duis aliquam nibh</li>
      <li><svg width="7" height="7" viewBox="0 0 8 8"><circle cx="4" cy="4" r="4" fill="#555"/><path d="M4 3.3v3" stroke="#fff" stroke-width="1.2"/><circle cx="4" cy="2" r=".7" fill="#fff"/></svg>Dui iaculis viverra id a velit</li>
      <li><svg width="7" height="7" viewBox="0 0 8 8"><circle cx="4" cy="4" r="4" fill="#555"/><path d="M4 3.3v3" stroke="#fff" stroke-width="1.2"/><circle cx="4" cy="2" r=".7" fill="#fff"/></svg>Vivamus egestas risus in</li>
      <li><svg width="7" height="7" viewBox="0 0 8 8"><circle cx="4" cy="4" r="4" fill="#555"/><path d="M4 3.3v3" stroke="#fff" stroke-width="1.2"/><circle cx="4" cy="2" r=".7" fill="#fff"/></svg>Magna varius commodo</li>
      <li><svg width="7" height="7" viewBox="0 0 8 8"><circle cx="4" cy="4" r="4" fill="#555"/><path d="M4 3.3v3" stroke="#fff" stroke-width="1.2"/><circle cx="4" cy="2" r=".7" fill="#fff"/></svg>Sed semper viverra</li>
      <li><svg width="7" height="7" viewBox="0 0 8 8"><circle cx="4" cy="4" r="4" fill="#555"/><path d="M4 3.3v3" stroke="#fff" stroke-width="1.2"/><circle cx="4" cy="2" r=".7" fill="#fff"/></svg>Egestas lobortis turpis</li>
    </ul>
    <div class="more-btn">SEE MORE</div>
  </div>
</section>

<section class="about">
  <div class="about-text">
    <h2>ABOUT CORVA MUSIC</h2>
    <p>Aliquam molestie, mi et imperdiet euismod, dui purus auctor tellus, et interdum lacus lectus et ante. Sed accumsan sollicitudin sapien, sit amet adipiscing turpis gravida ac. In congue, neque ac lobortis volutpat, libero mauris varius mi, vitae suscipit ipsum ligula vitae risus. Duis aliquam nibh a dui iaculis viverra id a velit. Vivamus egestas risus in magna varius commodo. Sed semper viverra egestas. Etiam pretium porttitor lectus, vel ornare neque porta volutpat.</p>
    <a href="#">Read More</a>
  </div>
  <form class="signup">
    <h3>SIGN UP FOR UPDATES</h3>
    <p>Aliquam molestie, mi et imperdiet dui purus auctor...</p>
    <input type="email" placeholder="Enter Email Address">
    <button type="button">SIGN UP</button>
  </form>
</section>

<footer class="site-footer">
  <p>Please review the Terms of use carefully before using Corva Music</p>
  <p>By accessing or using Corva Music, you express your understanding and acceptance of the Terms of use including the Privacy policy</p>
  <p class="copyright">Copyright © 2016. Corva Music. All Right Reserved</p>
  <div class="social"><i></i><i></i><i></i></div>
</footer>
</body>
</html>
```